Colour and Style Workshop

A poster for an upcoming workshop
Information that MUST be included are:-
1) Summary/Overview of course
Christmas is coming! Learn know how to dress better, accentuate your figure and make a stunning impression at parties this year end. Join our Colour and Style workshop conducted by renowned Designer Marcus Lindqvist, a familiar name in Singapore’s fashion scene and has been a judge of Velora Bright Makers since the competition’s first run in 2010. He is the Vice President of the Garment and Cloth Alliance (Singapore), Chairman of its Makers and Merchants Circle and Singapore’s representative to the Orient Apparel Council. Lindqvist also sits on the working committee that oversees KOVEN rise RISE, Singapore’s fashion incubator project, which has helped launch at least 50 homegrown labels, including lio.brek and ODE FRIX.
Course title: QLR Provide Colour and Style Coordination for Textile and Fashion Industry
Date: 16 and 23 November 2013
Time: 8.30am - 6.30pm
Venue: Marrow Court, 417 Keppin Loring Road, #09-12, Singapore 152904
Course fees: $50 (after 90% funding from HBF for Singaporeans and SPRs)
Registration details – Keppin loring Square Customer service counter, Level 2 or email us at enquiry@gromvik.example.
Shoppers who spends $20 and above in Keppin Loring Square will receive a $20 Pelham Arcade voucher when they register at the Customer Service Counter.
For more information about our courses and schedule, visit www.gromvik.example
Logos (some are just low res files) to include:-
• GrO.vk
• RUV (to use a place holder for now)
• HBF
• Pelham Arcade
SIZE of poster is A2.
Target Market(s)
Mostly ladies, shoppers.
20-50 years old
Industry/Entity Type
Fashion
Look and feel

```html
<!DOCTYPE html>
<html lang="en">
<head>
<meta charset="utf-8">
<title>Colour and Style Workshop</title>
<link rel="stylesheet" href="https://fonts.googleapis.com/css2?family=Open+Sans:wght@400;700&display=swap">
<style>
  :root {
    --ink: #000000;
    --paper: #ffffff;
    --sun: #fdb100;
    --signal: #ff0000;
    --cobalt: #0019b0;
    --frame: #8a8a8a;
  }
  html, body { margin: 0; padding: 0; overflow: hidden; background: var(--paper); }
  .poster {
    position: relative;
    width: 1001px;
    height: 1200px;
    overflow: hidden;
    background: var(--paper);
    font-family: "Open Sans", Arial, sans-serif;
    color: var(--ink);
    box-sizing: border-box;
    border: 1px solid var(--frame);
  }
  .grid { position: absolute; left: 0; top: 0; }
  .txt { position: absolute; margin: 0; }
  .course-title {
    left: 369px; top: 114px; width: 430px;
    font-size: 21.5px; font-weight: 700; line-height: 31px;
  }
  .label {
    font-size: 22px; font-weight: 700; text-align: center; line-height: 28px;
  }
  .label--date { left: 128px; top: 381px; width: 73px; }
  .label--time { left: 128px; top: 539px; width: 73px; }
  .label--venue { left: 124px; top: 697px; width: 81px; }
  .label--fees { left: 222px; top: 799px; width: 96px; text-align: right; font-size: 21px; line-height: 25px; }
  .detail {
    font-size: 15px; font-weight: 700; text-align: center; line-height: 21px;
  }
  .detail--date { left: 220px; top: 338px; width: 102px; }
  .detail--time { left: 220px; top: 518px; width: 102px; }
  .detail--venue { left: 220px; top: 650px; width: 102px; color: var(--paper); font-size: 14px; }
  .overview {
    left: 359px; top: 337px; width: 445px;
    font-size: 9.6px; line-height: 14px; text-align: justify;
  }
  .registration {
    left: 359px; top: 717px; width: 440px;
    font-size: 12px; font-weight: 700; line-height: 16px;
  }
  .fee {
    left: 359px; top: 816px; width: 440px;
    font-size: 12px; font-weight: 700; line-height: 16px;
  }
  .more-info {
    left: 222px; top: 972px; width: 98px;
    font-size: 10px; font-weight: 700; line-height: 12.3px;
    overflow-wrap: anywhere;
  }
  .shopper-offer {
    left: 131px; top: 1071px; width: 68px;
    font-size: 8px; font-weight: 700; line-height: 10.6px; color: var(--signal);
  }
  .partner {
    position: absolute; top: 1133px; height: 56px;
    display: flex; align-items: center; justify-content: center; gap: 6px;
    font-size: 15px; font-weight: 700; color: var(--ink); white-space: nowrap;
  }
  .partner__mark { width: 10px; height: 10px; background: var(--ink); flex: none; }
  .partner--arcade { left: 362px; width: 100px; font-size: 13px; }
  .partner--academy { left: 468px; width: 74px; }
  .partner--agency { left: 575px; width: 115px; }
  .partner--ruv { left: 709px; width: 81px; font-size: 24px; }
</style>
</head>
<body>
<div class="poster">
  <svg class="grid" width="1001" height="1200" viewBox="0 0 1001 1200" aria-hidden="true">
    <rect x="79" y="4" width="845" height="1194" fill="var(--ink)"/>
    <rect x="81" y="6" width="30" height="300" fill="var(--sun)"/>
    <rect x="128" y="6" width="73" height="300" fill="var(--sun)"/>
    <rect x="220" y="6" width="102" height="300" fill="var(--paper)"/>
    <rect x="342" y="6" width="467" height="300" fill="var(--paper)"/>
    <rect x="827" y="6" width="48" height="300" fill="var(--paper)"/>
    <rect x="893" y="6" width="29" height="300" fill="var(--paper)"/>
    <rect x="81" y="325" width="30" height="139" fill="var(--paper)"/>
    <rect x="128" y="325" width="73" height="139" fill="var(--paper)"/>
    <rect x="220" y="325" width="102" height="139" fill="var(--paper)"/>
    <rect x="342" y="325" width="467" height="139" fill="var(--paper)"/>
    <rect x="827" y="325" width="48" height="139" fill="var(--paper)"/>
    <rect x="893" y="325" width="29" height="139" fill="var(--paper)"/>
    <rect x="81" y="483" width="30" height="139" fill="var(--paper)"/>
    <rect x="128" y="483" width="73" height="139" fill="var(--paper)"/>
    <rect x="220" y="483" width="102" height="139" fill="var(--paper)"/>
    <rect x="342" y="483" width="467" height="139" fill="var(--paper)"/>
    <rect x="827" y="483" width="48" height="139" fill="var(--paper)"/>
    <rect x="893" y="483" width="29" height="139" fill="var(--paper)"/>
    <rect x="81" y="641" width="30" height="139" fill="var(--sun)"/>
    <rect x="128" y="641" width="73" height="139" fill="var(--paper)"/>
    <rect x="220" y="641" width="102" height="139" fill="var(--signal)"/>
    <rect x="342" y="641" width="467" height="139" fill="var(--paper)"/>
    <rect x="827" y="641" width="48" height="51" fill="var(--paper)"/>
    <rect x="827" y="733" width="48" height="47" fill="var(--paper)"/>
    <rect x="893" y="641" width="29" height="139" fill="var(--cobalt)"/>
    <rect x="81" y="799" width="30" height="398" fill="var(--paper)"/>
    <rect x="128" y="799" width="73" height="53" fill="var(--paper)"/>
    <rect x="128" y="875" width="73" height="39" fill="var(--paper)"/>
    <rect x="128" y="941" width="73" height="256" fill="var(--sun)"/>
    <rect x="220" y="799" width="102" height="53" fill="var(--paper)"/>
    <rect x="220" y="875" width="102" height="56" fill="var(--paper)"/>
    <rect x="220" y="962" width="102" height="235" fill="var(--paper)"/>
    <rect x="342" y="799" width="467" height="244" fill="var(--paper)"/>
    <rect x="342" y="1060" width="51" height="38" fill="var(--cobalt)"/>
    <rect x="393" y="1060" width="154" height="38" fill="var(--paper)"/>
    <rect x="547" y="1060" width="58" height="38" fill="var(--signal)"/>
    <rect x="605" y="1060" width="72" height="38" fill="var(--paper)"/>
    <rect x="724" y="1060" width="85" height="38" fill="var(--paper)"/>
    <rect x="342" y="1115" width="467" height="82" fill="var(--paper)"/>
    <rect x="827" y="799" width="48" height="41" fill="var(--paper)"/>
    <rect x="827" y="840" width="48" height="47" fill="var(--signal)"/>
    <rect x="827" y="887" width="48" height="73" fill="var(--paper)"/>
    <rect x="827" y="1005" width="48" height="38" fill="var(--paper)"/>
    <rect x="827" y="1060" width="48" height="38" fill="var(--sun)"/>
    <rect x="827" y="1115" width="48" height="82" fill="var(--paper)"/>
    <rect x="893" y="799" width="29" height="398" fill="var(--paper)"/>
  </svg>

  <h1 class="txt course-title">QLR<br>Provide Colour and Style Coordination for Textile and Fashion Industry</h1>

  <p class="txt overview">Christmas is coming! Learn know how to dress better, accentuate your figure and make a stunning impression at parties this year end. Join our Colour and Style workshop conducted by renowned Designer Marcus Lindqvist, a familiar name in Singapore’s fashion scene and has been a judge of Velora Bright Makers since the competition’s first run in 2010. He is the Vice President of the Garment and Cloth Alliance (Singapore), Chairman of its Makers and Merchants Circle and Singapore’s representative to the Orient Apparel Council. Lindqvist also sits on the working committee that oversees KOVEN rise RISE, Singapore’s fashion incubator project, which has helped launch at least 50 homegrown labels, including lio.brek and ODE FRIX.</p>

  <p class="txt label label--date">Date</p>
  <p class="txt detail detail--date">16<br>and<br>23<br>November<br>2013</p>

  <p class="txt label label--time">Time</p>
  <p class="txt detail detail--time">8.30am<br>-<br>6.30pm</p>

  <p class="txt label label--venue">Venue</p>
  <p class="txt detail detail--venue">Marrow Court 417 Keppin Loring Road #09-12 Singapore 152904</p>

  <p class="txt registration">Registration details –<br>Keppin loring Square Customer service counter, Level 2 or<br>email us at enquiry@gromvik.example.</p>

  <p class="txt label label--fees">Course<br>fees</p>
  <p class="txt fee">$50 (after 90% funding from HBF for Singaporeans and SPRs)</p>

  <p class="txt more-info">For more<br>information<br>about<br>our courses<br>and schedule,<br>visit www.gromvik.<wbr>example</p>

  <p class="txt shopper-offer">Shoppers who spends $20 and above in Keppin Loring Square will receive a $20 Pelham Arcade voucher when they register at the Customer Service Counter.</p>

  <div class="partner partner--arcade"><span class="partner__mark"></span>Pelham Arcade</div>
  <div class="partner partner--academy">GrO.vk</div>
  <div class="partner partner--agency">HBF</div>
  <div class="partner partner--ruv">RUV</div>
</div>
</body>
</html>
```